KEV.PRO- Darren Holcombe Fitness- needs a clever business card using the logo, name, info, contact

I need a business card designed for my Online Personal Training company called KEV.PRO, abbreviation for Darren Holcombe Fitness. My company focuses on coaching in personal health and personal growth to unleash your greatest potential. I would like to see designs that use my color scheme of a redish-orange (C:0,M:84,Y:100,K:0), grey, white, black, and my company font is OSWALD. The final design should communicate some aspects of design, health, motivation, growth, in some way. The logo is very important to the company and can be displayed in any of the colors previously mentioned. Must include the company name, my website: www.kev-pro.example , my email: dan@kev-pro.example

Target Market(s)

Personal health, fitness, general public, those who lack knowledge, awareness, and confidence in personal health

Industry/Entity Type

Personal Trainer

Font styles to use
Other font styles liked:
• OSWALD. (Bold, Regular, Light)

Colors
f37122
ffffff
9d9d9d
000000

Requirements
Must have
• Must include the logo, company name, my website: www.kev-pro.example , my email: dan@kev-pro.example
Nice to have
• Variations of the colors scheme of a redish-orange (C:0,M:84,Y:100,K:0), grey, white, black. Logo, card, or text can be in any of these colors.
• Possible quote like "Take control of your personal health to unleash your greatest potential" or "Unleashing your greatness first begins with fitness of the body and mind"

```html
<!DOCTYPE html>
<html lang="en">
<head>
<meta charset="utf-8">
<title>KEV.PRO Business Card</title>
<link href="https://fonts.googleapis.com/css2?family=Oswald:wght@300;400;600;700&display=swap" rel="stylesheet">
<style>
  :root {
    --orange: #e9521f;
    --ink: #242022;
    --paper: #f7f7f7;
    --white: #ffffff;
    --stage: #6b6b6b;
    --text-light: #e4e4e4;
  }
  html, body {
    margin: 0;
    padding: 0;
    width: 1200px;
    height: 1134px;
    overflow: hidden;
    background: var(--stage);
    font-family: "Oswald", sans-serif;
  }
  .canvas { position: relative; width: 1200px; height: 1134px; }
  .card {
    position: absolute;
    left: 261px;
    width: 676px;
    height: 380px;
    border-radius: 14px;
    overflow: hidden;
    background: var(--ink);
  }
  .card--front { top: 161px; }
  .card--back { top: 590px; }
  .card__art { position: absolute; inset: 0; }

  .brand { position: absolute; text-align: center; }
  .brand__dot {
    display: block;
    margin: 0 auto 22px;
    width: 150px;
    height: 150px;
    border-radius: 50%;
    background: var(--orange);
  }
  .brand__name {
    display: block;
    font-weight: 600;
    font-size: 36px;
    line-height: 1;
    letter-spacing: 0.2px;
  }
  .brand__tagline {
    display: block;
    margin-top: 3px;
    font-weight: 400;
    font-size: 10px;
    letter-spacing: -0.1px;
    text-transform: uppercase;
  }
  .brand--front { left: 96px; top: 84px; width: 160px; color: var(--ink); }
  .brand--back { left: 258px; top: 73px; width: 160px; color: var(--white); }

  .details { position: absolute; left: 411px; top: 74px; color: var(--text-light); }
  .details__name {
    margin: 0;
    font-weight: 600;
    font-size: 34px;
    line-height: 1.1;
    color: var(--orange);
    letter-spacing: 0.3px;
  }
  .details__role { margin: 0; font-weight: 300; font-size: 20px; line-height: 1.2; color: var(--white); }
  .details__address { margin: 52px 0 0; font-weight: 300; font-size: 15px; line-height: 23px; font-style: normal; }
  .contact { list-style: none; margin: 24px 0 0; padding: 0; font-weight: 300; font-size: 15px; }
  .contact__item { display: flex; align-items: center; height: 23px; }
  .contact__icon { width: 16px; height: 16px; margin-right: 8px; fill: var(--orange); }
</style>
</head>
<body>
<main class="canvas">

  <section class="card card--front" aria-label="Business card front">
    <svg class="card__art" viewBox="0 0 676 380" aria-hidden="true">
      <path d="M0 0 H308 Q415 175 268 380 H0 Z" fill="var(--paper)"/>
      <path d="M340 72 Q425 235 290 380 L268 380 Q400 225 340 72 Z" fill="var(--orange)"/>
    </svg>

    <div class="brand brand--front">
      <span class="brand__dot"></span>
      <span class="brand__name">KEV.PRO</span>
      <span class="brand__tagline">Darren Holcombe Fitness</span>
    </div>

    <div class="details">
      <h1 class="details__name">ALAN MERCER</h1>
      <p class="details__role">President</p>
      <address class="details__address">Level 2, 17 Harbour Lane<br>Eastwick, VIC 3999</address>
      <ul class="contact">
        <li class="contact__item">
          <svg class="contact__icon" viewBox="0 0 16 16"><path d="M3.5 1.5l2.5 0 1 3.5-1.6 1.2c.8 1.8 2.2 3.2 4 4l1.2-1.6 3.5 1v2.5c0 .8-.7 1.4-1.5 1.4C6.8 13.5 2.5 9.2 2.1 3 2.1 2.2 2.7 1.5 3.5 1.5z"/></svg>
          555 014 2290
        </li>
        <li class="contact__item">
          <svg class="contact__icon" viewBox="0 0 16 16"><path d="M1.5 3.5h13v1.2L8 8.8 1.5 4.7z"/><path d="M1.5 6.2L8 10.3l6.5-4.1v6.3h-13z"/></svg>
          dan@kev-pro.example
        </li>
        <li class="contact__item">
          <svg class="contact__icon" viewBox="0 0 16 16"><path d="M8 1a7 7 0 100 14A7 7 0 008 1zm0 1.5c.8 0 1.7 1.5 2 4H6c.3-2.5 1.2-4 2-4zM2.6 6.5h2c-.1.5-.1 1-.1 1.5s0 1 .1 1.5h-2a5.5 5.5 0 010-3zM6 9.5h4c-.3 2.5-1.2 4-2 4s-1.7-1.5-2-4zm5.4 0h2a5.5 5.5 0 000-3h-2c.1.5.1 1 .1 1.5s0 1-.1 1.5z"/></svg>
          www.kev-pro.example
        </li>
      </ul>
    </div>
  </section>

  <section class="card card--back" aria-label="Business card back">
    <div class="brand brand--back">
      <span class="brand__dot"></span>
      <span class="brand__name">KEV.PRO</span>
      <span class="brand__tagline">Darren Holcombe Fitness</span>
    </div>
  </section>

</main>
</body>
</html>
```